Stationery Design Project for Marketing Consultancy

I have started a new consultancy business and require the following elements to be designed using existing logo:
• Business card
• Letterhead
• Envelope (DL, C4, C5)
• Microsoft word template for report writing
• A4 Presentation Folder
• Powerpoint template
COPY FOR FRONT AND BACK OF BUSINESS CARD
logo
'Countable Growth. Bold Outcomes' slogan (but no need to use existing lockup with logo)
name, B Bus. Mktg, Grad Dip Digital Mktg, CPM (post nominal abbreviations in smaller font)
mobile: 04XX-XXX-XXX (I will give details to the winner to add)
website: www.quorvale.com.au
email: info@quorvale.com.au
COPY FOR LETTERHEAD
Logo
Company Name
Please, submit your designs that include business card, letterhead and envelope. Once selected the winner will be asked to complete the project by creating the rest of the artwork.
FINAL FILES
Print ready files to be supplied as well as Indesign files so that minor amends can be made if necessary in future.
• Layered vectors in EPS & PDF
• Screen quality JPEG & PNGs
ABOUT THE BUSINESS: QUORVALE
I work with clients to understand their business challenges, developing and executing measurable marketing strategies tied to key business metrics. Services include:
Services include:
• Business planning and business development
• Marketing and brand strategy
• Insight-driven integrated campaigns
• Loyalty programs and retention marketing
• Marketing automation
• Direct marketing (traditional and digital)
• Content strategy and development
Hi everyone,
Target Market(s)
Corporate decision makers (heads of marketing, general managers etc) and small to medium sized business owners. Predominately male aged 35+
Industry/Entity Type
Marketing
Requirements
Must have
- BRAND PERSONALITY
The successful design will communicate brand personality. I am a professional, results-driven entrepreneur, but want to show off my creative flair.
MEMORABILITY
Looking for a unique and eye-catching design. Am considering special printing effects (die cuts, letterpress, interactive elements, embossing, foiling etc) or a striking minimalist approach.
Nice to have
- I have a mission that could be incorporated on reverse if room -
Turning insights into actions & passion into profit.
Should not have
- Use of pink or green.

```html
<!DOCTYPE html>
<html lang="en">
<head>
<meta charset="utf-8">
<title>Quorvale Stationery</title>
<link rel="stylesheet" href="https://fonts.googleapis.com/css2?family=Lato:wght@300;400;700;900&family=Dancing+Script&display=swap">
<style>
  :root {
    --teal: #57c1cf;
    --teal-dark: #3fa9b8;
    --paper: #ffffff;
    --ink: #2f2f2f;
    --ink-soft: #555555;
    --backdrop: #ecebe8;
  }
  * { box-sizing: border-box; margin: 0; padding: 0; }
  html, body { width: 1200px; height: 900px; overflow: hidden; }
  body {
    background: var(--backdrop);
    font-family: 'Lato', sans-serif;
    color: var(--ink);
    position: relative;
  }
  .sheet { position: absolute; border-radius: 10px; box-shadow: 0 3px 10px rgba(0,0,0,.18); overflow: hidden; }

  /* Letterhead */
  .letterhead { left: 177px; top: 45px; width: 486px; height: 660px; background: var(--paper); }
  .brand-mark { display: flex; align-items: center; gap: 6px; color: var(--teal); font-weight: 900; letter-spacing: .04em; }
  .brand-mark .dot { width: 12px; height: 12px; border-radius: 50%; background: currentColor; }
  .letterhead .brand-mark { position: absolute; left: 50px; top: 60px; font-size: 16px; }
  .salutation { position: absolute; left: 52px; top: 193px; font-size: 12px; }
  .letter-body { position: absolute; left: 52px; top: 220px; width: 358px; font-size: 7.6px; line-height: 11.4px; color: var(--ink-soft); text-align: justify; }
  .letter-body p + p { margin-top: 11px; }
  .signoff { position: absolute; left: 52px; top: 444px; }
  .signoff .name { font-size: 11px; }
  .signoff .role { font-size: 7px; color: var(--ink-soft); margin-top: 6px; }
  .signature { position: absolute; left: 40px; top: 495px; width: 90px; height: 45px; background: linear-gradient(90deg, rgba(47,47,47,.12), rgba(47,47,47,.04)); border-radius: 4px; }
  .contact-list { list-style: none; font-size: 7.5px; color: var(--teal); }
  .contact-list li { display: flex; align-items: center; gap: 5px; height: 11px; }
  .contact-list svg { width: 8px; height: 8px; flex: none; }
  .letterhead .contact-list { position: absolute; left: 50px; top: 600px; }
  .tagline { font-size: 10px; color: var(--teal); text-transform: uppercase; letter-spacing: .02em; }
  .tagline strong { font-weight: 700; }
  .letterhead .tagline { position: absolute; left: 204px; top: 624px; }

  /* Folder */
  .folder { left: 690px; top: 45px; width: 487px; height: 663px; background: linear-gradient(160deg, #63c9d6, var(--teal) 60%, #4fb8c6); }
  .folder-pocket { position: absolute; inset: 0; }
  .folder .brand-mark { position: absolute; left: 198px; top: 210px; color: var(--paper); font-size: 14px; }
  .wordmark { color: var(--paper); font-weight: 900; letter-spacing: .02em; line-height: 1; }
  .folder .wordmark { position: absolute; left: 16px; bottom: 12px; font-size: 78px; }

  /* Business cards */
  .card { top: 733px; width: 247px; height: 129px; border-radius: 12px; }
  .card-front { left: 33px; background: var(--teal); }
  .card-front .dot-mark { position: absolute; left: 114px; top: 22px; width: 20px; height: 20px; border-radius: 50%; background: var(--paper); }
  .card-front .wordmark { position: absolute; left: 10px; bottom: 10px; font-size: 38px; }
  .card-back { left: 303px; background: var(--paper); }
  .card-back .tagline { position: absolute; left: 16px; top: 16px; font-size: 8px; }
  .card-back .holder { position: absolute; left: 16px; top: 60px; }
  .holder .name { color: var(--teal); font-weight: 700; font-size: 11px; }
  .holder .quals { font-size: 4.5px; color: var(--ink-soft); margin-top: 2px; }
  .card-back .contact-list { position: absolute; left: 16px; top: 88px; font-size: 6.5px; color: var(--teal); }
  .card-back .contact-list li { height: 9px; }
  .card-back .contact-list svg { width: 6px; height: 6px; }
</style>
</head>
<body>

<svg width="0" height="0" style="position:absolute">
  <defs>
    <symbol id="icon-phone" viewBox="0 0 10 10"><circle cx="5" cy="5" r="4.3" fill="none" stroke="currentColor"/><path d="M3.4 2.8l1 .9-.5.7a3 3 0 0 0 1.7 1.7l.7-.5.9 1-.8.6A4 4 0 0 1 2.8 3.6z" fill="currentColor"/></symbol>
    <symbol id="icon-web" viewBox="0 0 10 10"><circle cx="5" cy="5" r="4.3" fill="none" stroke="currentColor"/><circle cx="5" cy="5" r="2" fill="none" stroke="currentColor" stroke-width=".8"/></symbol>
    <symbol id="icon-mail" viewBox="0 0 10 10"><circle cx="5" cy="5" r="4.3" fill="none" stroke="currentColor"/><rect x="2.8" y="3.5" width="4.4" height="3" fill="none" stroke="currentColor" stroke-width=".7"/><path d="M2.8 3.5L5 5.2 7.2 3.5" fill="none" stroke="currentColor" stroke-width=".7"/></symbol>
  </defs>
</svg>

<article class="sheet letterhead">
  <div class="brand-mark"><span class="dot"></span>QUORVALE</div>
  <p class="salutation">Dear Mr. Hartley,</p>
  <div class="letter-body">
    <p>Lorem ipsum dolor sit amet, consectetur adipiscing elit. Donec orci purus, luctus vitae dignissim eu, iaculis sed purus. Vivamus faucibus, ipsum nec aliquet viverra, leo mauris condimentum ligula, sit amet sagittis enim ligula quis arcu. Nam egestas tortor id nisi porttitor mattis. In tortor ante, ultricies in suscipit a, tempus non massa. Vivamus et auctor mi. Fusce vel massa nulla. Phasellus nec eros mauris, et scelerisque orci. Donec malesuada orci vitae nulla accumsan porta a id massa. Quisque accumsan iaculis magna sit amet fringilla. Maecenas consequat, magna eget tincidunt semper, odio nibh rutrum mi, id feugiat ante nisl eu risus. Vestibulum nunc orci, rhoncus a placerat in, ultricies in mi. Cras mattis varius eros, vel fringilla nisi suscipit eget.</p>
    <p>Quisque scelerisque sagittis nulla at porttitor. Mauris a justo et tellus interdum tristique. Sed id augue vitae urna euismod commodo aliquet a quam. Pellentesque arcu velit, cursus et malesuada ut, consequat et diam. Nullam erat sem, rhoncus id ullamcorper vitae, rhoncus et arcu. In ultricies ultricies nulla, ut rutrum nisl iaculis at. Donec eu magna a sapien sagittis faucibus. Fusce aliquet faucibus ultricies. Morbi semper, est id tincidunt gravida, sem arcu adipiscing lacus, ac bibendum nulla leo eu purus. Quisque nec diam sed risus consectetur tincidunt. Nam quis nibh. Vestibulum id purus lorem.</p>
  </div>
  <div class="signoff">
    <p class="name">Liam Archer</p>
    <p class="role">Co-Founder &amp; CEO</p>
  </div>
  <div class="signature" role="img" aria-label="Handwritten signature of Liam Archer"></div>
  <ul class="contact-list">
    <li><svg><use href="#icon-phone"/></svg>04XX-XXX-XXX</li>
    <li><svg><use href="#icon-web"/></svg>www.quorvale.com.au</li>
    <li><svg><use href="#icon-mail"/></svg>info@quorvale.com.au</li>
  </ul>
  <p class="tagline">Countable Growth. <strong>Bold Outcomes.</strong></p>
</article>

<article class="sheet folder">
  <svg class="folder-pocket" viewBox="0 0 487 663" preserveAspectRatio="none" aria-hidden="true">
    <path d="M487 140 L470 140 Q455 140 455 160 L455 300 Q455 320 470 320 L487 320" fill="rgba(255,255,255,.12)" stroke="rgba(0,0,0,.12)"/>
  </svg>
  <div class="brand-mark"><span class="dot"></span>QUORVALE</div>
  <p class="wordmark">QUORVALE</p>
</article>

<article class="sheet card card-front">
  <span class="dot-mark"></span>
  <p class="wordmark">QUORVALE</p>
</article>

<article class="sheet card card-back">
  <p class="tagline">Countable Growth. <strong>Bold Outcomes.</strong></p>
  <div class="holder">
    <p class="name">Owen Pellard</p>
    <p class="quals">B Bus. Mktg, Grad Dip Digital Mktg, CPM</p>
  </div>
  <ul class="contact-list">
    <li><svg><use href="#icon-phone"/></svg>04XX-XXX-XXX</li>
    <li><svg><use href="#icon-web"/></svg>www.quorvale.com.au</li>
    <li><svg><use href="#icon-mail"/></svg>info@quorvale.com.au</li>
  </ul>
</article>

</body>
</html>
```